Qorvant Flyer Design Project

We need a new flyer design for our company based in Australia. We provide Business Valuations for small businesses. The flyer should follow the same colours and theme as our website www.qorvant.com.au and our logo. The design should communicate a professional financial services company. It should be a simple design (not too 'busy') and have a sleek and professional feel to it. It will be used to send to prospective clients and referral sources to tell about our company and prompt them to call us or visit our website.

Target Market(s)

Business owners and people working in financial services (accountants, financial planners etc)

Industry/Entity Type

Financial

Requirements
Must have
• Must be DL double sided, (99mm x 210mm) and use CMYK colours. Must contain trim marks for printer and be print ready.

```html
<!DOCTYPE html>
<html lang="en">
<head>
<meta charset="utf-8">
<title>Qorvant DL Flyer – Front and Back</title>
<link href="https://fonts.googleapis.com/css2?family=Arimo:wght@400;700&display=swap" rel="stylesheet">
<style>
  :root {
    --navy: #2a3990;
    --blue: #1f7fc4;
    --green: #8db23a;
    --ink: #5a5f6b;
    --paper: #ffffff;
    --backdrop: #ecebe8;
    --photo-dark: #25303f;
    --photo-mid: #7d8a99;
    --photo-light: #c9d0d8;
  }
  * { box-sizing: border-box; margin: 0; padding: 0; }
  html, body { width: 1200px; height: 873px; overflow: hidden; }
  body {
    background: var(--backdrop);
    font-family: "Arimo", Arial, sans-serif;
    position: relative;
  }
  .flyer {
    position: absolute;
    top: 118px;
    width: 300px;
    height: 636px;
    background: var(--paper);
    overflow: hidden;
    box-shadow: 0 4px 14px rgba(0,0,0,.18);
  }
  .flyer--front { left: 235px; }
  .flyer--back { left: 665px; }

  /* Brand lockup */
  .brand { display: flex; align-items: center; }
  .brand__dot { border-radius: 50%; background: var(--blue); flex: none; }
  .brand__name { color: var(--navy); font-weight: 700; letter-spacing: -.3px; }

  .flyer--front .brand { flex-direction: column; margin-top: 34px; }
  .flyer--front .brand__dot { width: 54px; height: 54px; }
  .flyer--front .brand__name { font-size: 22px; margin-top: 4px; }

  .headline {
    margin-top: 46px;
    text-align: center;
    color: var(--navy);
    font-size: 20px;
    line-height: 1.18;
    font-weight: 400;
  }
  .headline strong { font-weight: 700; }

  /* Photo areas */
  .photo {
    position: absolute;
    left: 0; right: 0; bottom: 0;
  }
  .photo__fill { position: absolute; inset: 0; }
  .photo__curve { position: absolute; left: 0; top: 0; width: 300px; display: block; }

  .flyer--front .photo { top: 262px; }
  .flyer--front .photo__fill {
    background:
      radial-gradient(ellipse at 30% 85%, rgba(141,178,58,.55), transparent 45%),
      linear-gradient(160deg, var(--photo-dark) 0%, var(--photo-mid) 35%, var(--photo-light) 55%, var(--photo-mid) 75%, var(--photo-dark) 100%);
  }
  .url {
    position: absolute;
    left: 30px; bottom: 22px;
    color: #fff;
    font-size: 11px;
  }

  .flyer--back .photo { top: 392px; }
  .flyer--back .photo__fill {
    background:
      radial-gradient(ellipse at 30% 70%, rgba(141,178,58,.55), transparent 40%),
      linear-gradient(100deg, var(--photo-dark) 0%, var(--photo-mid) 30%, var(--photo-light) 55%, var(--photo-mid) 78%, var(--photo-dark) 100%);
  }

  /* Back content */
  .reasons { padding: 30px 26px 0 40px; }
  .reasons__title {
    color: var(--navy);
    font-size: 15px;
    font-weight: 700;
    margin-bottom: 12px;
  }
  .reasons__list { list-style: none; }
  .reasons__list li {
    position: relative;
    padding-left: 6px;
    color: var(--ink);
    font-size: 9.6px;
    line-height: 1.3;
    margin-bottom: 6px;
  }
  .reasons__list li::before {
    content: "";
    position: absolute;
    left: -2px; top: 5px;
    width: 3px; height: 3px;
    border-radius: 50%;
    background: var(--navy);
  }

  .contact {
    position: absolute;
    left: 30px; top: 346px;
    display: flex;
    align-items: center;
    gap: 12px;
    color: var(--navy);
    font-size: 9.6px;
    line-height: 1.35;
  }
  .contact .brand { flex-direction: column; }
  .contact .brand__dot { width: 24px; height: 24px; }
  .contact .brand__name { font-size: 9px; margin-top: 1px; }
  .contact__group { display: flex; flex-direction: column; }
  .contact__row { display: flex; align-items: center; gap: 4px; }
  .contact__row svg { width: 9px; height: 9px; flex: none; }
  .contact__divider { width: 1px; height: 26px; background: var(--navy); opacity: .6; }
</style>
</head>
<body>

<section class="flyer flyer--front" aria-label="Flyer front">
  <div class="brand">
    <span class="brand__dot"></span>
    <span class="brand__name">qorvant</span>
  </div>
  <h1 class="headline">The Expert for<br>Your <strong>Business Valuation</strong></h1>

  <div class="photo">
    <div class="photo__fill" role="img" aria-label="Monochrome photo of a team stacking hands together, with a soft green tint"></div>
    <svg class="photo__curve" viewBox="0 0 300 50" height="50" aria-hidden="true">
      <path d="M0 0 H300 V42 Q150 -8 0 42 Z" fill="#ffffff"/>
    </svg>
    <p class="url">www.qorvant.com.au</p>
  </div>
</section>

<section class="flyer flyer--back" aria-label="Flyer back">
  <div class="reasons">
    <h2 class="reasons__title">Why use Qorvant?</h2>
    <ul class="reasons__list">
      <li>Qualified Accountant spends time reviewing every business</li>
      <li>Specialised – valuing small businesses is all we do</li>
      <li>We use our experience to compare and benchmark similar businesses across Australia</li>
      <li>A valuation appraisal report emailed to you with our comments and valuation estimate</li>
      <li>Five business day turnaround!</li>
      <li>A follow up phone call from an Accountant to discuss the valuation and answer any questions you have</li>
      <li>Fixed price of only $540 (+gst)</li>
      <li>Our clients include Business Buyers and Sellers, Accountants, Solicitors, Financial Planners, Franchisors and Franchisees</li>
    </ul>
  </div>

  <div class="photo">
    <div class="photo__fill" role="img" aria-label="Monochrome photo of smiling business people in suits, with a soft green tint"></div>
    <svg class="photo__curve" viewBox="0 0 300 80" height="80" aria-hidden="true">
      <path d="M0 0 H300 V14 Q150 110 0 14 Z" fill="#ffffff"/>
    </svg>
  </div>

  <div class="contact">
    <div class="brand">
      <span class="brand__dot"></span>
      <span class="brand__name">qorvant</span>
    </div>
    <div class="contact__group">
      <span class="contact__row">
        <svg viewBox="0 0 10 10" aria-hidden="true"><path d="M1 3 Q5 0 9 3 L8 4.5 L6.5 3.8 V3 H3.5 V3.8 L2 4.5 Z M2.5 5 H7.5 L8.5 9 H1.5 Z" fill="currentColor"/></svg>
        1300 555 014
      </span>
      <span class="contact__row">
        <svg viewBox="0 0 10 10" aria-hidden="true"><rect x="2.5" y="1" width="5" height="3" fill="none" stroke="currentColor"/><rect x="1" y="4" width="8" height="4.5" fill="currentColor"/></svg>
        07 5550 0172
      </span>
    </div>
    <span class="contact__divider"></span>
    <div class="contact__group">
      <span class="contact__row">
        <svg viewBox="0 0 10 10" aria-hidden="true"><rect x="1" y="2" width="8" height="6" fill="none" stroke="currentColor"/><path d="M1 2 L5 5.5 L9 2" fill="none" stroke="currentColor"/></svg>
        info@qorvant.com.au
      </span>
      <span class="contact__row">ABN – 41 902 318 765</span>
    </div>
  </div>
</section>

</body>
</html>
```